Harborline Stay Collective Business Card Design

Design a business card for Harborline Stay Collective. Look at the website for colors and reference. Card should have logo, name, title, office number, mobile number, email, URL and a tagline like, "Luxury Hotel & Resort Email Marketing" (This might change).

https://www.harborlinestaycollective.net

The rest I will leave up to your imagination.

Contact Information for Business Card

Logo, name, title, office number, mobile number, email, URL and a tagline like, "Luxury Hotel & Resort Email Marketing" (This might change).

```html
<!DOCTYPE html>
<html lang="en">
<head>
<meta charset="utf-8">
<title>Harborline Stay Collective – Business Card</title>
<link rel="stylesheet" href="https://fonts.googleapis.com/css2?family=Arimo:wght@400;700&display=swap">
<style>
  :root {
    --orange: #f47621;
    --ink: #1c1c1c;
    --paper: #ffffff;
    --backdrop: #3a3836;
  }
  * { box-sizing: border-box; margin: 0; padding: 0; }
  html, body { width: 1200px; height: 900px; overflow: hidden; }
  body {
    background: var(--backdrop);
    font-family: "Arimo", Arial, sans-serif;
    position: relative;
  }
  .card {
    position: absolute;
    left: 320px;
    width: 560px;
    height: 320px;
    border-radius: 22px;
    overflow: hidden;
    box-shadow: 0 10px 24px rgba(0,0,0,.45);
  }
  .card-back { top: 100px; background: var(--orange); }
  .card-front { top: 480px; background: var(--paper); }

  .back-brand {
    position: absolute;
    inset: 0;
    padding: 0 60px;
    display: flex;
    align-items: center;
    justify-content: center;
    text-align: center;
    color: var(--paper);
    font-weight: 700;
    font-size: 34px;
    line-height: 1.2;
    letter-spacing: 1px;
    text-transform: uppercase;
  }

  .front-brand {
    position: absolute;
    left: 36px;
    top: 100px;
    display: flex;
    align-items: center;
    gap: 10px;
    color: var(--ink);
    font-weight: 700;
    font-size: 19px;
    text-transform: uppercase;
    letter-spacing: .5px;
  }
  .front-brand .brand-square {
    width: 14px; height: 14px; background: var(--orange);
  }

  .person {
    position: absolute;
    right: 36px;
    top: 38px;
    text-align: right;
  }
  .person-name {
    color: var(--orange);
    font-weight: 700;
    font-size: 22px;
    text-transform: uppercase;
  }
  .person-title { color: var(--ink); font-size: 15px; margin-top: 3px; }

  .tagline {
    position: absolute;
    right: 36px;
    top: 168px;
    text-align: right;
    color: var(--ink);
    font-size: 15px;
    line-height: 1.3;
  }

  .contacts {
    position: absolute;
    left: 76px;
    top: 172px;
    list-style: none;
    color: var(--ink);
    font-size: 14px;
  }
  .contacts li { display: flex; align-items: center; gap: 8px; height: 22px; white-space: nowrap; }
  .contacts svg { width: 14px; height: 14px; flex: none; }

  .stripes { position: absolute; left: 0; bottom: 0; width: 560px; height: 90px; }
  .site-url {
    position: absolute;
    right: 20px;
    bottom: 24px;
    color: var(--paper);
    font-size: 12px;
    white-space: nowrap;
  }
</style>
</head>
<body>
  <section class="card card-back" aria-label="Card back">
    <div class="back-brand">Harborline Stay Collective</div>
  </section>

  <section class="card card-front" aria-label="Card front">
    <div class="front-brand"><span class="brand-square"></span>Harborline Stay Collective</div>

    <div class="person">
      <p class="person-name">Marcus Ellery</p>
      <p class="person-title">Co-Founder</p>
    </div>

    <p class="tagline">Luxury Hotel &amp; Resort<br>Email Marketing</p>

    <ul class="contacts">
      <li>
        <svg viewBox="0 0 16 16" fill="var(--orange)"><path d="M1 6c0-2 3-4 7-4s7 2 7 4v1h-4V5.5C10 5 6 5 5 5.5V7H1z"/><rect x="3" y="8" width="10" height="6" rx="1"/></svg>
        555-210-4789
      </li>
      <li>
        <svg viewBox="0 0 16 16" fill="none" stroke="var(--orange)" stroke-width="1.6"><rect x="4" y="1" width="8" height="14" rx="1.5"/><line x1="7" y1="12.5" x2="9" y2="12.5"/></svg>
        555-384-9087
      </li>
      <li>
        <svg viewBox="0 0 16 16" fill="none" stroke="var(--orange)" stroke-width="1.6"><rect x="1" y="3" width="14" height="10"/><polyline points="1,3 8,9 15,3"/></svg>
        info@harborlinestaycollective.net
      </li>
    </ul>

    <svg class="stripes" viewBox="0 0 560 90" aria-hidden="true">
      <polygon points="0,64 322,42 322,47 0,69" fill="var(--orange)"/>
      <polygon points="0,74 322,52 318,90 0,90" fill="var(--ink)"/>
      <polygon points="0,84 318,84 317,90 0,90" fill="var(--orange)"/>
      <polygon points="330,18 560,18 560,90 322,90" fill="var(--orange)"/>
    </svg>
    <p class="site-url">www.harborlinestaycollective.net</p>
  </section>
</body>
</html>
```